Garden of Eden - Digital Party Invite

I'm throwing a Halloween party with the theme "Garden of Eden". The invite will be sent via Tidewell Cards. I need a custom design for the invite. Here are the details:
The image needs to be 670x970.
Needs to be sexy - maybe with Adam & Eve, and the snake w/the apple, etc
Text should be:
You Are Invited To
The Garden of Eden
Sat Oct 26 7:00PM
at
Dinah & Tobias's Home
612 North Birch Rd 7B
Costumes Highly Encouraged
Adults Only Please

```html
<!DOCTYPE html>
<html lang="en">
<head>
<meta charset="utf-8">
<title>The Garden of Eden – Party Invitation</title>
<link rel="stylesheet" href="https://fonts.googleapis.com/css2?family=Cinzel:wght@400;500;600;700&family=Montserrat:wght@600&display=swap">
<style>
  :root {
    --paper: #ffffff;
    --ink: #111111;
    --crimson: #c1272d;
    --wash-gold: #f1ebaa;
    --wash-peach: #f3dfc3;
    --canopy: #5fa35c;
    --canopy-light: #8cc27a;
    --fence: #d9a060;
    --blossom: #e07a4a;
    --grass: #a3cc82;
    --grass-light: #d8e8b4;
  }
  * { margin: 0; padding: 0; box-sizing: border-box; }
  html, body {
    width: 915px;
    height: 1200px;
    overflow: hidden;
    background: var(--paper);
  }
  .invite {
    position: relative;
    width: 915px;
    height: 1200px;
    background: var(--paper);
    overflow: hidden;
    color: var(--ink);
  }
  .sky-wash {
    position: absolute;
    left: 0; top: 0;
    width: 915px; height: 470px;
    background: linear-gradient(to bottom, var(--wash-gold) 0%, #f4ecc4 45%, var(--wash-peach) 72%, rgba(255,255,255,0) 100%);
  }
  .meadow {
    position: absolute;
    left: 0; bottom: 0;
    width: 915px; height: 330px;
    background: linear-gradient(to bottom, rgba(255,255,255,0) 0%, #f3efc8 35%, var(--grass-light) 70%, var(--grass) 100%);
  }
  .grove {
    position: absolute;
    bottom: 0;
    height: 340px;
    background: linear-gradient(to bottom, var(--canopy-light) 0%, var(--canopy) 38%, var(--blossom) 56%, var(--fence) 66%, var(--fence) 84%, var(--grass) 100%);
  }
  .grove-left {
    left: 0; width: 320px;
    border-top-right-radius: 140px 110px;
  }
  .grove-right {
    right: 0; width: 315px; height: 350px;
    border-top-left-radius: 140px 110px;
  }
  .content {
    position: absolute;
    inset: 0;
    text-align: center;
  }
  .lead-in {
    position: absolute;
    top: 182px; left: 0; width: 100%;
    font-family: "Montserrat", sans-serif;
    font-weight: 600;
    font-size: 30px;
    line-height: 1;
    text-transform: uppercase;
  }
  .title {
    position: absolute;
    left: 0; width: 100%;
    font-family: "Cinzel", serif;
    line-height: 1;
  }
  .title-top {
    top: 212px;
    color: var(--crimson);
    font-size: 100px;
    font-weight: 500;
  }
  .title-bottom {
    top: 316px;
    font-size: 97px;
    font-weight: 600;
  }
  .date {
    position: absolute;
    top: 0; left: 0; width: 100%; height: 100%;
    font-family: "Cinzel", serif;
    font-weight: 500;
  }
  .date-part {
    position: absolute;
    top: 511px;
    font-size: 50px;
    line-height: 1;
  }
  .date-month { right: 555px; }
  .date-year { left: 540px; }
  .date-day {
    position: absolute;
    left: 386px; width: 140px;
    top: 467px;
    font-size: 100px;
    line-height: 1;
  }
  .date-time {
    position: absolute;
    left: 386px; width: 140px;
    top: 569px;
    font-size: 22px;
    line-height: 1;
  }
  .date-rule {
    position: absolute;
    top: 489px;
    width: 2px; height: 96px;
    background: var(--ink);
  }
  .date-rule.left { left: 386px; }
  .date-rule.right { left: 525px; }
  .venue {
    position: absolute;
    top: 650px; left: 0; width: 100%;
    font-family: "Cinzel", serif;
    font-weight: 500;
    font-size: 35px;
    line-height: 38px;
  }
  .notes {
    position: absolute;
    top: 800px; left: 0; width: 100%;
    font-family: "Cinzel", serif;
    font-weight: 500;
    color: var(--crimson);
    font-size: 27px;
    line-height: 28px;
  }
</style>
</head>
<body>
  <main class="invite">
    <div class="sky-wash" role="img" aria-label="Soft watercolour sky in pale gold and peach with a few birds in flight"></div>
    <div class="meadow" role="img" aria-label="Watercolour meadow of soft green grass fading into a pale horizon"></div>
    <div class="grove grove-left" role="img" aria-label="Watercolour trees above a wooden fence with red and orange flowers"></div>
    <div class="grove grove-right" role="img" aria-label="Watercolour trees above a wooden fence with red and orange flowers"></div>

    <section class="content">
      <p class="lead-in">You are invited to</p>
      <h1 class="title title-top">The Garden</h1>
      <h1 class="title title-bottom">of Eden</h1>

      <div class="date">
        <span class="date-part date-month">10</span>
        <span class="date-rule left"></span>
        <span class="date-day">26</span>
        <span class="date-time">7:00 PM</span>
        <span class="date-rule right"></span>
        <span class="date-part date-year">24</span>
      </div>

      <p class="venue">Dinah &amp; Tobias's Home<br>612 North Birch Rd 7B</p>

      <p class="notes">Costumes Highly Encouraged<br>Adults Only Please</p>
    </section>
  </main>
</body>
</html>
```